Need a new design for Glass Cleaner label. The brand name already exists i.e. BRIXO. Pell is the company name. Looking for new design. It's application is for cleaning glasses in houses, cars, offices e.t.c. Our product gives streak free shine and anti static effect. Images of old label design is attached. Bottle will be same as before. It's better to show a car as well in the design but not necessary. New logo's of brixo can also be designed.

Target Market(s)

Household and automobile

Industry/Entity Type

It Company

```html
<!DOCTYPE html>
<html lang="en">
<head>
<meta charset="utf-8">
<title>Brixo Glass Cleaner Label</title>
<link rel="stylesheet" href="https://fonts.googleapis.com/css2?family=Oswald:wght@500;700&family=Open+Sans:wght@400&display=swap">
<style>
  :root {
    --page: #ffffff;
    --ink: #1a1a1a;
    --label-red: #e31e24;
    --label-navy: #16237a;
    --label-blue: #1f4fb4;
    --label-yellow: #ffe600;
    --label-white: #ffffff;
  }
  html, body {
    margin: 0;
    padding: 0;
    width: 922px;
    height: 1200px;
    overflow: hidden;
    background: var(--page);
  }
  .artboard {
    position: relative;
    width: 922px;
    height: 1200px;
  }
  .dimension {
    position: absolute;
    font-family: "Open Sans", sans-serif;
    font-size: 20px;
    color: var(--ink);
  }
  .dimension-width {
    left: 190px;
    top: 140px;
    width: 520px;
    border-bottom: 2px solid var(--ink);
    text-align: center;
    padding-bottom: 6px;
  }
  .dimension-height {
    left: 740px;
    top: 200px;
    height: 875px;
    border-left: 2px solid var(--ink);
  }
  .dimension-height span {
    position: absolute;
    left: 10px;
    top: 50%;
    transform: translateY(-50%) rotate(90deg);
    transform-origin: left center;
    white-space: nowrap;
    margin-left: 12px;
  }
  .label {
    position: absolute;
    left: 190px;
    top: 200px;
    width: 520px;
    height: 875px;
  }
  .label text { font-family: "Oswald", sans-serif; }
  .brand-name { font-weight: 700; fill: var(--label-red); }
  .company-name { font-weight: 700; fill: var(--label-red); }
  .new-flag { font-weight: 700; fill: var(--label-yellow); }
  .tag-title { font-weight: 700; fill: var(--label-yellow); }
  .tag-claim { font-weight: 500; fill: var(--label-navy); }
  .volume { font-weight: 700; font-style: italic; fill: var(--label-white); }
</style>
</head>
<body>
<main class="artboard">
  <div class="dimension dimension-width">76 mm</div>
  <div class="dimension dimension-height"><span>127.5 mm</span></div>

  <svg class="label" viewBox="0 0 410 690" xmlns="http://www.w3.org/2000/svg" aria-label="Brixo glass cleaner front label">
    <defs>
      <radialGradient id="label-field" cx="0.55" cy="0.5" r="0.7">
        <stop offset="0" stop-color="#2c63c9"/>
        <stop offset="0.6" stop-color="var(--label-blue)"/>
        <stop offset="1" stop-color="var(--label-navy)"/>
      </radialGradient>
      <linearGradient id="scene-fill" x1="0" y1="0" x2="0" y2="1">
        <stop offset="0" stop-color="#9fc3de"/>
        <stop offset="0.55" stop-color="#7d8f6a"/>
        <stop offset="1" stop-color="#5f8a3a"/>
      </linearGradient>
    </defs>

    <path class="label-border" fill="var(--label-red)"
      d="M330,6 Q358,-8 380,12 Q404,40 407,90 L410,600 Q410,684 340,686 L70,686 Q0,684 0,612 L2,290 Q5,238 42,204 L300,22 Z"/>
    <path class="label-field" fill="url(#label-field)"
      d="M338,30 Q360,22 374,40 Q392,66 394,105 L396,598 Q396,670 336,672 L76,672 Q14,670 14,610 L16,300 Q20,256 54,226 L312,42 Z"/>
    <path class="stitch-line" fill="none" stroke="var(--label-yellow)" stroke-width="1.6" stroke-dasharray="6 4"
      d="M340,16 Q365,8 380,28 Q398,56 400,98 L403,600 Q403,678 338,679 L72,679 Q6,677 7,610 L9,294 Q12,246 48,214 L306,32 Z"/>

    <path class="logo-corner" fill="var(--label-yellow)"
      d="M188,212 L340,92 Q360,82 366,104 L372,190 Q372,212 350,212 Z"/>
    <text class="company-name" x="296" y="182" font-size="34" text-anchor="middle">Pell</text>

    <circle class="swoosh-ring" cx="225" cy="335" r="140" fill="none" stroke="var(--label-yellow)" stroke-width="3"
      stroke-dasharray="180 90 240 900"/>
    <text class="new-flag" x="280" y="250" font-size="34" text-anchor="middle" transform="rotate(-10 280 250)">New!</text>
    <text class="brand-name" x="205" y="375" font-size="108" text-anchor="middle" transform="rotate(-10 205 375)">BRIXO</text>

    <rect class="scene-photo" x="15" y="432" width="238" height="168" fill="url(#scene-fill)" stroke="#d9d9d9" stroke-width="5"
      role="img" aria-label="Hand wiping a window with a yellow cloth, red car parked on grass behind"/>

    <g class="product-tag" transform="rotate(-10 320 500)">
      <rect x="232" y="468" width="142" height="42" fill="var(--label-red)"/>
      <text class="tag-title" x="303" y="499" font-size="24" text-anchor="middle">Glass Cleaner</text>
      <rect x="256" y="510" width="150" height="36" fill="var(--label-white)"/>
      <text class="tag-claim" x="331" y="536" font-size="20" text-anchor="middle">Streak Free Shine!</text>
    </g>

    <text class="volume" x="322" y="644" font-size="20" text-anchor="middle">500ml</text>
  </svg>
</main>
</body>
</html>
```